Marlow Vantage - Health, Wellness, Fitness Consultants

Marlow Vantage are Marlow Vantage are leading consultants to the Health, Wellness and Fitness industry​​, with over 25 years experience working with some of the biggest global worldwide brands from equipment providers and facility operators to mass participation events and obstacle course races. Marlow Vantage is a multi disciplined business specialising in helping brands grow through insight, strategy creation and valuable sector collaboration, We are the official exclusive distributors of Kinfor Rig bodyweight training products for the UK and Ireland, Official Partners of Obstacle Course Race and Adventure Racing Brindle Dash & Cobalt Trek Tour - I would like a black background card, 1 side Marlow Vantage logo only other side Official, Exclusive, Distributors and Partners in the UK & Ireland. Then list Brindle Dash, Kinfor Rig, Cobalt Trek Tour contact details at very bottom Founder / Director - Perry Dunmore
Mobile - +44(0)7900123456
E - Mail - perry.dunmore@marlowvantage.example
Web - www.marlowvantage.example
Skype - marlowvantage

```html
<!DOCTYPE html>
<html lang="en">
<head>
<meta charset="utf-8">
<title>Marlow Vantage – Business Card</title>
<link rel="stylesheet" href="https://fonts.googleapis.com/css2?family=Lato:wght@300;400;700;900&display=swap">
<style>
  :root {
    --stage: #2b2b2b;
    --card: #111111;
    --lime: #c3d23a;
    --text-light: #e8e8e8;
    --band: #ffffff;
    --partner-blue: #1d4f9c;
    --partner-dark: #1a1a1a;
    --partner-orange: #e5771e;
  }
  * { box-sizing: border-box; margin: 0; padding: 0; }
  html, body { width: 800px; height: 1200px; overflow: hidden; }
  body {
    background: var(--stage);
    font-family: "Lato", sans-serif;
    position: relative;
  }
  .card {
    position: absolute;
    left: 60px;
    width: 680px;
    height: 390px;
    background: var(--card);
    border-radius: 4px;
    box-shadow: 0 6px 18px rgba(0,0,0,.45);
    overflow: hidden;
  }
  .card--front { top: 150px; }
  .card--back { top: 660px; }

  /* Front */
  .brand-mark {
    position: absolute;
    inset: 0;
    display: flex;
    flex-direction: column;
    align-items: center;
    justify-content: center;
  }
  .brand-mark__name {
    font-weight: 700;
    font-size: 58px;
    color: var(--lime);
    letter-spacing: 1px;
  }
  .brand-mark__tagline {
    margin-top: 14px;
    font-weight: 400;
    font-size: 17px;
    color: var(--lime);
    letter-spacing: .5px;
  }

  /* Back */
  .contact {
    position: absolute;
    left: 40px;
    top: 34px;
  }
  .contact__name {
    font-weight: 900;
    font-size: 22px;
    color: var(--lime);
    letter-spacing: 1px;
    text-transform: uppercase;
  }
  .contact__role {
    font-size: 12px;
    color: var(--text-light);
    margin-top: 2px;
  }
  .contact__list {
    list-style: none;
    margin-top: 14px;
  }
  .contact__item {
    display: flex;
    align-items: center;
    gap: 9px;
    font-size: 12.5px;
    color: var(--text-light);
    line-height: 21px;
  }
  .contact__icon { width: 13px; height: 13px; flex: none; }

  .back-brand {
    position: absolute;
    right: 40px;
    top: 96px;
    text-align: left;
  }
  .back-brand__name {
    font-weight: 300;
    font-size: 34px;
    color: var(--lime);
  }
  .back-brand__tagline {
    font-size: 11.5px;
    color: var(--lime);
    margin-top: 2px;
  }

  .partner-band {
    position: absolute;
    left: 0; right: 0;
    top: 210px;
    height: 72px;
    background: var(--band);
    display: flex;
    align-items: center;
    justify-content: space-around;
    padding: 0 20px;
  }
  .partner {
    font-weight: 900;
    font-size: 30px;
    text-transform: uppercase;
    display: flex;
    align-items: center;
    gap: 8px;
  }
  .partner--kinfor { color: var(--partner-blue); }
  .partner--brindle { color: var(--partner-dark); }
  .partner--cobalt { color: var(--partner-orange); font-size: 16px; }
  .partner__badge {
    width: 30px; height: 30px;
    background: var(--partner-orange);
    border-radius: 50%;
  }

  .partner-statement {
    position: absolute;
    left: 0; right: 0;
    top: 310px;
    text-align: center;
    font-size: 17px;
    color: var(--lime);
  }
</style>
</head>
<body>

<section class="card card--front">
  <div class="brand-mark">
    <div class="brand-mark__name">Marlow Vantage</div>
    <div class="brand-mark__tagline">Health | Wellness | Fitness | Consultants</div>
  </div>
</section>

<section class="card card--back">
  <div class="contact">
    <div class="contact__name">Perry Dunmore</div>
    <div class="contact__role">Founder / Director</div>
    <ul class="contact__list">
      <li class="contact__item">
        <svg class="contact__icon" viewBox="0 0 16 16"><path fill="#c3d23a" d="M3.5 1l2.5 3-1.5 2c1 2 3 4 5 5l2-1.5 3 2.5-1.5 2.5C8 16 0 8 1 2.5z"/></svg>
        +44(0)7900123456
      </li>
      <li class="contact__item">
        <svg class="contact__icon" viewBox="0 0 16 16"><rect x="1" y="3" width="14" height="10" fill="#c3d23a"/><path d="M1 3l7 6 7-6" fill="none" stroke="#111" stroke-width="1.4"/></svg>
        perry.dunmore@marlowvantage.example
      </li>
      <li class="contact__item">
        <svg class="contact__icon" viewBox="0 0 16 16"><circle cx="8" cy="8" r="6.5" fill="none" stroke="#c3d23a" stroke-width="1.5"/><path d="M1.5 8h13M8 1.5c-3 3-3 10 0 13M8 1.5c3 3 3 10 0 13" fill="none" stroke="#c3d23a" stroke-width="1.2"/></svg>
        www.marlowvantage.example
      </li>
      <li class="contact__item">
        <svg class="contact__icon" viewBox="0 0 16 16"><circle cx="8" cy="8" r="7" fill="#c3d23a"/></svg>
        marlowvantage
      </li>
    </ul>
  </div>

  <div class="back-brand">
    <div class="back-brand__name">Marlow Vantage</div>
    <div class="back-brand__tagline">Health, Wellness, Fitness, Consultants</div>
  </div>

  <div class="partner-band">
    <div class="partner partner--kinfor">Kinfor Rig</div>
    <div class="partner partner--brindle">Brindle Dash</div>
    <div class="partner partner--cobalt"><span class="partner__badge"></span>Cobalt Trek Tour</div>
  </div>

  <p class="partner-statement">Official, Exclusive, Distributors and Partners in the UK &amp; Ireland</p>
</section>

</body>
</html>
```